LADIES' HORIZON ALLIANCE

Design a website for a membership based organization focusing on entrepreneurship, women's issues and global news regarding commerce.
Also, want a news daily tie in to site, and social media outlets.
I want the colors in strong blue, deep or metallic gold and cream/white like logo which will be provided. I want logo altered with globe to replace small sphere in the design.
Also, board members page that should be redesigned. Might need extra coding.
PLEASE SEE http://ladieshorizonalliance.example DIDN'T LIKE THIS LAY OUT AT ALL TOO MUCH WHITE AND NOT ENOUGH IMPACT. WANT TO DRAW MEMBERS.

PLEASE SEE http://www.tqrb-example.com/Index.cfm BUT THIS IS WAY TO BUSY BUT I LIKE THE SLIDING.

SEE OUR TWITTER ACCOUNT FOR INSIGHT. @LADIESHORALL

Reason: Happy Holidays. The board approving the design will be out on season time vacation until Jan. 2. Please make any edits requested from designer already submitting layouts. Thank you, Delphine

Target Market(s)

GLOBAL BUSINESS WOMEN AND ENTREPRENEURS AGES 20-65

Industry/Entity Type

Media

Number of Pages Required

4 page

Font styles to use
Other font styles liked:
• Baskerville or something similar

Colors
fbed22
3377b5
9bcb3c

Requirements
Must have
• Show diversity of ethnicities if using stock photos. Vibrant and inviting site, MUST JOIN or Be part of this organization. Luxury style
• THIS IS A FOR PROFIT WEBSITE.
• Membership Fees:
• Annual Fee $250
• For an additional fee of $150 you can grow your visibility and voice through our Ladies' Horizon Alliance Newsletter and Speaker's Bureau (LHANSB).
• LHA Speaker's Bureau will support your personal, business and organizations' objectives and to give you greater visibility and voice as an authority world leader or business visionary in your field of service.
• LHASB realizes that so many worthy leaders' in diverse fields of service are never allowed to be heard. If you feel you are a dynamic speaker, run a worthwhile business or organization and whose wisdom and success can be of service of others sign up today and be part of the LHASB!
• Student Membership
• Discounted student memberships are also available. Students have access to selected group forums, as well as selected groups of members that provide mentoring. Mentoring helps continue the member's legacy and creates a well spring of future leaders. Student membership fees cost just $75 a year.
• Contact us to help promote you and other women's vision throughout the world.
• Join LHA Now!
• CAN YOU PROVIDE A HEADLINE WITHOUT WOMEN SEE TWITTER ACCOUNT.
Nice to have
• Nice headline and well position tabs.
• Home
• Join LHA Now
• Memberships
• LHA Team Leadership
• About Us
• Contact
• LHA is an Effective Women's Alliance for You!
• New Member - Women's Organization
• 20% Discount- Offer Valid on Your Membership Fee When You Join before 1/30/2105
• Memberships
• LHA Leadership
• At Ladies' Horizon Alliance, we offer the opportunity to connect with women throughout the globe. Join these trailblazers to shorten your path to success and camaraderie.
• Who We Are
• Ladies' Horizon Alliance is an online women's initiative that promotes your business and visions through social engagement. We are here to help you form strategic partnerships with like-minded women around the world. End your solo journey by becoming a member of LHA.
• LHA also features a forum to promote the services, campaigns, and social activism by our members.
• LHA is about women helping other women. Contact us for more information.
• Learn More about Ladies' Horizon Alliance
• Contact us for more information in regards to LHA membership and how to get involved.
• SHARE THIS PAGE:
• twitter, fb, instagram, etc.

```html
<!DOCTYPE html>
<html lang="en">
<head>
<meta charset="utf-8">
<title>Ladies' Horizon Alliance</title>
<link href="https://fonts.googleapis.com/css2?family=Open+Sans:ital,wght@0,400;0,600;0,700;1,400;1,800&display=swap" rel="stylesheet">
<style>
:root{
  --blue:#0b6cc0;
  --blue-deep:#0862b2;
  --blue-text:#1166b5;
  --gold:#f6bd22;
  --gold-text:#f2b51d;
  --page:#eeeeee;
  --white:#ffffff;
  --ink:#222222;
  --grey:#7a7a7a;
  --line:#d8d8d8;
}
*{margin:0;padding:0;box-sizing:border-box}
html,body{width:1066px;height:1200px;overflow:hidden}
body{background:var(--page);font-family:'Open Sans',Arial,sans-serif;position:relative;color:var(--ink)}
.top-rule{position:absolute;left:0;top:0;width:1066px;height:3px;background:var(--blue)}
.sheet{position:absolute;left:87px;top:3px;width:891px;height:881px;background:var(--white)}
.abs{position:absolute}

/* header */
.brand{left:106px;top:58px;display:flex;flex-direction:column;align-items:flex-start}
.brand-dot{width:26px;height:26px;border-radius:50%;background:var(--gold);margin:0 0 6px 50px}
.brand-name{font-size:12.5px;font-weight:400;color:var(--ink);letter-spacing:-.3px}
.cta{top:24px;height:30px;width:104px;border-radius:3px;color:var(--white);font-size:11.5px;font-weight:600;display:flex;align-items:center;justify-content:center}
.cta-members{left:738px;background:var(--blue)}
.cta-leaders{left:857px;background:var(--gold)}
.main-nav{left:466px;top:75px;width:495px;display:flex;justify-content:space-between;list-style:none;font-size:11px;font-weight:600}
.main-nav li{color:#2a2a2a}
.main-nav .is-active{color:var(--gold-text)}

/* hero */
.hero{left:104px;top:118px;width:857px;height:440px;background:linear-gradient(100deg,#e9e3dc 0%,#d9c2ae 30%,#c9d3dc 55%,#b79c8a 75%,#8d9aa8 100%)}
.hero-title{left:550px;top:282px;width:400px;color:var(--white);font-style:italic;font-weight:800;font-size:34px;line-height:42px;text-shadow:2px 2px 4px rgba(0,0,0,.55);letter-spacing:-.5px;white-space:nowrap}
.hero-arrow{top:490px;width:39px;height:32px;background:rgba(40,40,40,.65);display:flex;align-items:center;justify-content:center}
.hero-prev{left:851px}.hero-next{left:896px}
.hero-shadow{left:130px;top:560px;width:806px;height:28px;background:radial-gradient(ellipse at top,rgba(0,0,0,.35),rgba(0,0,0,0) 70%)}

/* welcome */
.section-title{font-size:22px;font-weight:700;color:var(--blue-text);letter-spacing:-.2px}
.section-title span{color:var(--gold-text)}
.welcome-title{left:104px;top:596px}
.welcome-photo{left:104px;top:648px;width:182px;height:151px;border:2px solid #ddd;background:linear-gradient(135deg,#e6e9ee,#bfb3a7 55%,#d8dde3)}
.welcome-copy{left:304px;top:644px;width:352px;font-family:Arial,Helvetica,sans-serif;font-size:10.3px;line-height:18.4px;color:var(--grey);text-align:justify;hyphens:auto}
.welcome-copy p+p{margin-top:18.4px}
.btn-read{left:105px;top:819px;width:83px;height:32px;background:var(--gold);color:var(--white);font-family:Arial,sans-serif;font-size:11px;display:flex;align-items:center;justify-content:center}

/* tweets */
.tweets{left:682px;top:595px;width:280px;height:255px;border:1px solid var(--line);padding:20px 14px 0 22px}
.tweet{display:flex;gap:10px;padding:9px 0 10px}
.tweet+.tweet{border-top:1px solid var(--line);padding-top:12px}
.tweet-mark{flex:0 0 16px;height:16px;border-radius:50%;background:var(--blue);margin-top:2px}
.tweet-body{font-family:Arial,sans-serif;font-size:10px;line-height:18.4px;color:var(--grey)}
.tweet-body em{color:var(--blue-text)}
.tweet-time{color:var(--gold-text)}

/* footer */
.footer{left:0;top:884px;width:1066px;height:252px;background:var(--blue)}
.footer-bar{left:0;top:1136px;width:1066px;height:64px;background:var(--blue-deep)}
.foot-title{top:912px;color:var(--white);font-size:17.5px;font-weight:400}
.foot-links{left:105px;top:952px;list-style:none;color:var(--white);font-size:10.5px;line-height:18.4px}
.foot-about{left:245px;top:958px;width:206px;color:var(--white);font-size:9.8px;line-height:18.4px;text-align:justify;letter-spacing:-.15px}
.news-lead{left:497px;top:958px;width:246px;color:var(--white);font-size:10.8px;font-weight:600;line-height:17px;letter-spacing:-.1px}
.news-field{left:496px;top:1012px;width:211px;height:34px;border:1px solid var(--white);border-radius:3px;display:flex;align-items:center;justify-content:space-between;padding:2px 2px 2px 11px}
.news-field span{color:var(--white);font-size:9.5px;font-style:italic}
.news-go{width:35px;height:28px;background:var(--gold);border-radius:2px;display:flex;align-items:center;justify-content:center}
.legal{left:497px;top:1065px;color:var(--white);font-family:Arial,sans-serif;font-size:8px}
.legal u{margin:0 5px}
.legal u:first-child{margin-left:0}
.field{left:766px;width:196px;border:1px solid var(--white);border-radius:3px;color:var(--white);font-size:10px;padding:7px 12px}
.btn-submit{left:911px;top:1096px;width:51px;height:20px;background:var(--gold);border-radius:3px;color:var(--white);font-size:9px;font-weight:700;display:flex;align-items:center;justify-content:center}
.copyright{left:104px;top:1160px;color:var(--white);font-size:10.5px}
.social{left:772px;top:1160px;display:flex;gap:19px}
.social i{width:16px;height:16px;border-radius:3px;background:var(--white);display:block}
</style>
</head>
<body>
<div class="top-rule"></div>
<div class="sheet"></div>

<header>
  <div class="abs brand"><span class="brand-dot"></span><span class="brand-name">Ladies' Horizon Alliance</span></div>
  <div class="abs cta cta-members">Memberships</div>
  <div class="abs cta cta-leaders">LHA Leadership</div>
  <ul class="abs main-nav">
    <li class="is-active">HOME</li><li>ABOUT US</li><li>WHO WE ARE</li><li>SERVICES</li><li>NEWS</li><li>CONTACT</li>
  </ul>
</header>

<section>
  <div class="abs hero" role="img" aria-label="Photo of a smiling businesswoman in a bright office"></div>
  <h1 class="abs hero-title">LHA IS AN EFFECTIVE<br>WOMEN'S ALLIANCE<br>FOR YOU!</h1>
  <div class="abs hero-arrow hero-prev"><svg width="10" height="16" viewBox="0 0 10 16"><path d="M8 1L2 8l6 7" fill="none" stroke="#fff" stroke-width="2"/></svg></div>
  <div class="abs hero-arrow hero-next"><svg width="10" height="16" viewBox="0 0 10 16"><path d="M2 1l6 7-6 7" fill="none" stroke="#fff" stroke-width="2"/></svg></div>
  <div class="abs hero-shadow"></div>
</section>

<section>
  <h2 class="abs section-title welcome-title">WELCOME TO <span>HORIZON ALLIANCE</span></h2>
  <div class="abs welcome-photo" role="img" aria-label="Portrait of a smiling businesswoman with arms crossed"></div>
  <div class="abs welcome-copy" lang="en">
    <p>Ladies' Horizon Alliance is an online women's initiative that promotes your business and visions through social engagement. We are here to help you form strategic partnerships with like-minded women around the world. End your solo journey by becoming a member of LHA.</p>
    <p>LHA also features a forum to promote the services, campaigns, and social activism by our members. LHA is about women helping other women. Contact us for more information.</p>
  </div>
  <div class="abs btn-read">Read More</div>

  <aside class="abs tweets">
    <h2 class="section-title">LATEST <span>TWEETS</span></h2>
    <div style="height:10px"></div>
    <div class="tweet"><span class="tweet-mark"></span><p class="tweet-body"><em>Lorem ipsum dolor sit amet, consectetuer</em><br>adipiscing elit. Aenean commodo ligula eget Aenean massa. Cum sociis natoque<br><span class="tweet-time">1day ago</span></p></div>
    <div class="tweet"><span class="tweet-mark"></span><p class="tweet-body"><em>Lorem ipsum dolor sit amet, consectetuer</em><br>adipiscing elit. Aenean commodo ligula eget Aenean massa. Cum sociis natoque<br><span class="tweet-time">1day ago</span></p></div>
  </aside>
</section>

<footer>
  <div class="abs footer"></div>
  <div class="abs footer-bar"></div>
  <h3 class="abs foot-title" style="left:107px">NAVIGATION</h3>
  <ul class="abs foot-links"><li>Home</li><li>About</li><li>Who We Are</li><li>News</li><li>Services</li><li>Blog</li><li>News</li></ul>
  <h3 class="abs foot-title" style="left:243px">WHO WE ARE</h3>
  <p class="abs foot-about">Lorem ipsum dolor sit amet, consectetuer adipiscing elit. Aenean commodo ligula eget dolor. Aenean massa. Cum sociis natoque penatibus et magnis dis parturient montes, nascetur ridiculus mus. Donec quam felis, ultricies nec, pellentesque eu...</p>
  <h3 class="abs foot-title" style="left:497px">SIGN UP FOR NEWSLETTER</h3>
  <p class="abs news-lead">Sign up for our newsletter, and we'll keep you<br>updated on all events at Lumerra!</p>
  <div class="abs news-field"><span>enter your email address</span><span class="news-go"><svg width="6" height="9" viewBox="0 0 6 9"><path d="M1 1l3.5 3.5L1 8" fill="none" stroke="#fff" stroke-width="1.8"/></svg></span></div>
  <p class="abs legal"><u>Terms of Use</u>|<u>Privacy Policy</u></p>
  <h3 class="abs foot-title" style="left:760px">NEED MORE INFO?</h3>
  <div class="abs field" style="top:962px;height:26px">NAME</div>
  <div class="abs field" style="top:998px;height:25px">EMAIL</div>
  <div class="abs field" style="top:1033px;height:50px">MESSAGE</div>
  <div class="abs btn-submit">SUBMIT</div>
  <p class="abs copyright">© Copyright 2014 | Horizon Alliance. All rights reserved</p>
  <div class="abs social"><i></i><i></i><i></i><i></i><i></i><i></i></div>
</footer>
</body>
</html>
```